Newspaper Ad Design Project

Hi please see the attached newpaper pages (current) and the new layout in (publisher file). This is a new section in a local newspaper that is going to be branded as trelk.com.au (refer to our site for style etc. - and I've attached out logo. Note - it can be used in reverse as white on blue). This section is currently called "near ledger".
I have also attached a copy of one of our vouchers which will go in the top right of the newspaper section. We have allowed room for 8 of these. However, since mocking it up I have also realised we need a space for our own editorial (probably to the left of the vouchers - approx 2 columns wide - note : there are 7 vertical columns to a page on this newspaper). This editorial section should be up to 5 small business tips telling people to go to trelk for more info (so just a brief intro on each tip)
Tip : Keep it clean & simple. Don't over design it.

```html
<!DOCTYPE html>
<html lang="en">
<head>
<meta charset="utf-8">
<title>trelk – Business Directory</title>
<link href="https://fonts.googleapis.com/css2?family=Open+Sans:wght@400;600;700&family=Arimo:wght@400;700&family=Courier+Prime:wght@700&display=swap" rel="stylesheet">
<style>
  :root {
    --blue: #2597d2;
    --blue-deep: #1470bd;
    --blue-light: #3eaade;
    --ad-grey: #e6e6e6;
    --ink: #1a1a1a;
    --muted: #6a6a6a;
    --paper: #ffffff;
    --voucher-bg: #f3f7f8;
    --voucher-line: #b9c9d1;
  }
  * { box-sizing: border-box; margin: 0; padding: 0; }
  html, body { width: 1200px; height: 788px; overflow: hidden; background: var(--paper); }
  body { position: relative; font-family: "Open Sans", Arial, sans-serif; color: var(--ink); }

  .abs { position: absolute; }

  /* brand */
  .brand { position: absolute; width: 125px; }
  .brand-name { font-weight: 600; font-size: 46px; line-height: 40px; color: var(--blue); letter-spacing: -0.5px; }
  .brand-url { font-size: 10px; color: var(--muted); letter-spacing: 1px; margin-top: 4px; }

  /* masthead banners */
  .masthead {
    position: absolute; height: 50px; color: #fff;
    background: linear-gradient(90deg, var(--blue-light), var(--blue-deep));
    border-radius: 8px 8px 0 0;
  }
  .masthead-left .title { position: absolute; left: 13px; top: 4px; font-size: 17px; letter-spacing: 0.5px; }
  .masthead-left .slogan { position: absolute; right: 12px; top: 21px; font-size: 20px; letter-spacing: 0.5px; }
  .masthead-right { text-align: center; font-size: 15px; line-height: 20px; padding-top: 4px; letter-spacing: 0.5px; }

  /* section bars */
  .section-bar {
    position: absolute; height: 32px; background: var(--blue);
    color: #fff; font-weight: 700; font-size: 15px; line-height: 32px; padding-left: 18px; letter-spacing: 0.3px;
  }

  /* body copy */
  .copy { position: absolute; width: 212px; font-family: "Arimo", Arial, sans-serif; font-size: 10.6px; line-height: 12.1px; }
  .copy p + p { margin-top: 12px; }

  /* ad spaces */
  .ad { position: absolute; background: var(--ad-grey); display: flex; align-items: center; justify-content: center; font-size: 27px; color: var(--ink); }

  /* local deal panel */
  .deal-panel { position: absolute; left: 953px; top: 18px; width: 230px; height: 470px; border-radius: 8px; overflow: hidden;
    background: linear-gradient(90deg, var(--blue-light), var(--blue-deep)); }
  .deal-head { position: absolute; left: 0; top: 0; width: 230px; height: 74px; color: #fff; }
  .deal-head .label { position: absolute; left: 17px; top: 14px; font-weight: 700; font-size: 19px; line-height: 22px; }
  .deal-head .offer { position: absolute; right: 12px; top: 25px; font-size: 18px; }
  .deal-head .offer b { font-weight: 700; }
  .deal-foot { position: absolute; left: 0; bottom: 18px; width: 230px; text-align: center; color: #fff; font-size: 12px; }
  .deal-foot b { font-weight: 700; }

  .voucher-grid { position: absolute; left: 2px; top: 76px; width: 226px; height: 340px; background: var(--paper);
    display: grid; grid-template-columns: 1fr 1fr; grid-template-rows: repeat(4, 1fr); gap: 1px; }
  .voucher { position: relative; background: var(--voucher-bg); border: 1px dashed var(--voucher-line); font-family: "Arimo", Arial, sans-serif; text-align: center; }
  .voucher .v-brand { position: absolute; left: 3px; top: 2px; font-family: "Open Sans", Arial, sans-serif; font-weight: 600; font-size: 12px; line-height: 13px; color: var(--blue); }
  .voucher .v-off { position: absolute; right: 3px; top: 3px; width: 60px; height: 19px; border: 1px solid var(--blue); background: #fff;
    font-family: "Courier Prime", "Courier New", monospace; font-weight: 700; font-size: 12px; line-height: 17px; }
  .voucher .v-name { position: absolute; left: 0; right: 0; top: 25px; font-weight: 700; font-size: 7.2px; }
  .voucher .v-tiny { position: absolute; left: 0; right: 0; font-size: 3.4px; color: #444; }
  .voucher .v-deal { position: absolute; left: 0; right: 0; top: 44px; font-size: 6.4px; line-height: 7.4px; }
  .voucher .v-foot { position: absolute; left: 3px; right: 3px; bottom: 2px; display: flex; justify-content: space-between; font-size: 3.4px; color: #444; }
</style>
</head>
<body>

  <!-- left page -->
  <div class="brand" style="left:31px; top:26px;">
    <div class="brand-name">trelk</div>
    <div class="brand-url">www.trelk.com.au</div>
  </div>
  <header class="masthead masthead-left" style="left:150px; top:28px; width:391px;">
    <span class="title">Business Directory</span>
    <span class="slogan">Are you true trelk?</span>
  </header>

  <div class="section-bar" style="left:15px; top:94px; width:526px;">Editorial</div>

  <article class="copy" style="left:47px; top:145px;">
    <p>"Lorem ipsum dolor sit amet, consectetur adipisicing elit, sed do eiusmod tempor incididunt ut labore et dolore magna aliqua. Ut enim ad minim veniam, quis nostrud exercitation ullamco laboris nisi ut aliquip ex ea commodo consequat. Duis aute irure dolor in reprehenderit in voluptate velit esse cillum dolore eu fugiat nulla pariatur. Excepteur sint occaecat cupidatat non proident, sunt in culpa qui officia deserunt mollit anim id est laborum."</p>
    <p>"Lorem ipsum dolor sit amet, consectetur adipisicing elit, sed do eiusmod tempor incididunt ut labore et dolore magna aliqua. Ut enim ad minim veniam, quis nostrud exercitation ullamco laboris nisi ut aliquip ex ea commodo consequat. Duis aute irure dolor in reprehenderit in voluptate velit esse cillum dolore eu fugiat nulla pariatur. Excepteur sint occaecat cupidatat non proident, sunt in culpa qui officia deserunt mollit anim id est laborum."</p>
  </article>
  <article class="copy" style="left:283px; top:145px;">
    <p>"Lorem ipsum dolor sit amet, consectetur adipisicing elit, sed do eiusmod tempor incididunt ut labore et dolore magna aliqua. Ut enim ad minim veniam, quis nostrud exercitation ullamco laboris nisi ut aliquip ex ea commodo consequat. Duis aute irure dolor in reprehenderit in voluptate velit esse cillum dolore eu fugiat nulla pariatur. Excepteur sint occaecat cupidatat non proident, sunt in culpa qui officia deserunt mollit anim id est laborum."</p>
    <p>"Lorem ipsum dolor sit amet, consectetur adipisicing elit, sed do eiusmod tempor incididunt ut labore et dolore magna aliqua. Ut enim ad minim veniam, quis nostrud exercitation ullamco laboris nisi ut aliquip ex ea commodo consequat. Duis aute irure dolor in reprehenderit in voluptate velit esse cillum dolore eu fugiat nulla pariatur. Excepteur sint occaecat cupidatat non proident, sunt in culpa qui officia deserunt mollit anim id est laborum."</p>
  </article>

  <div class="ad" style="left:15px; top:512px; width:260px; height:128px;">Ads</div>
  <div class="ad" style="left:283px; top:512px; width:258px; height:128px;">Ads</div>
  <div class="ad" style="left:15px; top:648px; width:260px; height:127px;">Ads</div>
  <div class="ad" style="left:283px; top:648px; width:258px; height:127px;">Ads</div>

  <!-- right page -->
  <div class="brand" style="left:579px; top:26px;">
    <div class="brand-name">trelk</div>
    <div class="brand-url">www.trelk.com.au</div>
  </div>
  <header class="masthead masthead-right" style="left:703px; top:28px; width:238px;">
    Business Director<br>Supporting local business?
  </header>

  <div class="ad" style="left:566px; top:94px; width:137px; height:399px;">Ads</div>

  <div class="section-bar" style="left:711px; top:94px; width:234px;">Trelk Business Tips</div>
  <article class="copy" style="left:724px; top:145px;">
    <p>"Lorem ipsum dolor sit amet, consectetur adipisicing elit, sed do eiusmod tempor incididunt ut labore et dolore magna aliqua. Ut enim ad minim veniam, quis nostrud exercitation ullamco laboris nisi ut aliquip ex ea commodo consequat. Duis aute irure dolor in reprehenderit in voluptate velit esse cillum dolore eu fugiat nulla pariatur. Excepteur sint occaecat cupidatat non proident, sunt in culpa qui officia deserunt mollit anim id est laborum."</p>
    <p>"Lorem ipsum dolor sit amet, consectetur adipisicing elit, sed do eiusmod tempor incididunt ut labore et dolore magna aliqua. Ut enim ad minim veniam, quis nostrud exercitation ullamco laboris nisi ut aliquip ex ea commodo consequat. Duis aute irure dolor in reprehenderit in voluptate velit esse cillum dolore eu fugiat nulla pariatur. Excepteur sint occaecat cupidatat non proident, sunt in culpa qui officia deserunt mollit anim id est laborum."</p>
  </article>

  <section class="deal-panel">
    <div class="deal-head">
      <div class="label">LOCAL<br>DEAL</div>
      <div class="offer">Add on <b>FREE</b></div>
    </div>
    <div class="voucher-grid">
      <div class="voucher"><span class="v-brand">trelk</span><span class="v-off">50% OFF</span><div class="v-name">Steady Gear Riding School</div><div class="v-tiny" style="top:34px;">Hillcrest QLD</div><div class="v-tiny" style="top:39px;">Phone: 0400 000 111</div><div class="v-deal">FIRST LESSON HALF PRICE !<br>THAT'S JUST $35 p/hr.</div><div class="v-tiny" style="top:62px;">Valid for new riders only, one per visit</div><div class="v-foot"><span>ride@steadygear.example</span><span>Valid until 30 Dec</span></div></div>
      <div class="voucher"><span class="v-brand">trelk</span><span class="v-off">50% OFF</span><div class="v-name">Steady Gear Riding School</div><div class="v-tiny" style="top:34px;">Hillcrest QLD</div><div class="v-tiny" style="top:39px;">Phone: 0400 000 111</div><div class="v-deal">FIRST LESSON HALF PRICE !<br>THAT'S JUST $35 p/hr.</div><div class="v-tiny" style="top:62px;">Valid for new riders only, one per visit</div><div class="v-foot"><span>ride@steadygear.example</span><span>Valid until 30 Dec</span></div></div>
      <div class="voucher"><span class="v-brand">trelk</span><span class="v-off">50% OFF</span><div class="v-name">Steady Gear Riding School</div><div class="v-tiny" style="top:34px;">Hillcrest QLD</div><div class="v-tiny" style="top:39px;">Phone: 0400 000 111</div><div class="v-deal">FIRST LESSON HALF PRICE !<br>THAT'S JUST $35 p/hr.</div><div class="v-tiny" style="top:62px;">Valid for new riders only, one per visit</div><div class="v-foot"><span>ride@steadygear.example</span><span>Valid until 30 Dec</span></div></div>
      <div class="voucher"><span class="v-brand">trelk</span><span class="v-off">50% OFF</span><div class="v-name">Steady Gear Riding School</div><div class="v-tiny" style="top:34px;">Hillcrest QLD</div><div class="v-tiny" style="top:39px;">Phone: 0400 000 111</div><div class="v-deal">FIRST LESSON HALF PRICE !<br>THAT'S JUST $35 p/hr.</div><div class="v-tiny" style="top:62px;">Valid for new riders only, one per visit</div><div class="v-foot"><span>ride@steadygear.example</span><span>Valid until 30 Dec</span></div></div>
      <div class="voucher"><span class="v-brand">trelk</span><span class="v-off">50% OFF</span><div class="v-name">Steady Gear Riding School</div><div class="v-tiny" style="top:34px;">Hillcrest QLD</div><div class="v-tiny" style="top:39px;">Phone: 0400 000 111</div><div class="v-deal">FIRST LESSON HALF PRICE !<br>THAT'S JUST $35 p/hr.</div><div class="v-tiny" style="top:62px;">Valid for new riders only, one per visit</div><div class="v-foot"><span>ride@steadygear.example</span><span>Valid until 30 Dec</span></div></div>
      <div class="voucher"><span class="v-brand">trelk</span><span class="v-off">50% OFF</span><div class="v-name">Steady Gear Riding School</div><div class="v-tiny" style="top:34px;">Hillcrest QLD</div><div class="v-tiny" style="top:39px;">Phone: 0400 000 111</div><div class="v-deal">FIRST LESSON HALF PRICE !<br>THAT'S JUST $35 p/hr.</div><div class="v-tiny" style="top:62px;">Valid for new riders only, one per visit</div><div class="v-foot"><span>ride@steadygear.example</span><span>Valid until 30 Dec</span></div></div>
      <div class="voucher"><span class="v-brand">trelk</span><span class="v-off">50% OFF</span><div class="v-name">Steady Gear Riding School</div><div class="v-tiny" style="top:34px;">Hillcrest QLD</div><div class="v-tiny" style="top:39px;">Phone: 0400 000 111</div><div class="v-deal">FIRST LESSON HALF PRICE !<br>THAT'S JUST $35 p/hr.</div><div class="v-tiny" style="top:62px;">Valid for new riders only, one per visit</div><div class="v-foot"><span>ride@steadygear.example</span><span>Valid until 30 Dec</span></div></div>
      <div class="voucher"><span class="v-brand">trelk</span><span class="v-off">50% OFF</span><div class="v-name">Steady Gear Riding School</div><div class="v-tiny" style="top:34px;">Hillcrest QLD</div><div class="v-tiny" style="top:39px;">Phone: 0400 000 111</div><div class="v-deal">FIRST LESSON HALF PRICE !<br>THAT'S JUST $35 p/hr.</div><div class="v-tiny" style="top:62px;">Valid for new riders only, one per visit</div><div class="v-foot"><span>ride@steadygear.example</span><span>Valid until 30 Dec</span></div></div>
    </div>
    <div class="deal-foot">Add a deal for your Business <b>FREE</b></div>
  </section>

  <div class="ad" style="left:566px; top:512px; width:182px; height:188px;">Ads</div>
  <div class="ad" style="left:754px; top:512px; width:181px; height:188px;">Ads</div>
  <div class="ad" style="left:566px; top:708px; width:369px; height:67px;">Ads</div>
  <div class="ad" style="left:953px; top:512px; width:230px; height:263px;">Ads</div>

</body>
</html>
```